Verdalux Web Presence

I need a word press site for my company that houses diverse services, and am looking to profile these areas: Design and Delivery of Social Innovation Initiatives, Innovative Pubic Engagement, The Turquoise Economy, Youth Entrepreneurship, and The Science of Change.

I would also like to profile my recent projects. A blog, video and photos are also important features.

Industry/Entity Type

It Company

Requirements
Must have
• I would like to have an overview of what the company does as a Think, Feel and Do Company, along with sections for specific services and recent project profiles.

I would like a section for a blog

I would like a section for photos and video.

I would like the look and feel of the website to reflect the following:

Morwen has spent 30 years leading expeditions into the future. Morwen has a special interest in exploring the changing business, social and cultural landscapes and frontiers, uncovering uncharted territory and unleashing hidden potential – within the person, family, organization, community, business or marketplace. Morwen thrives on experimentation that has led to blended eastern and western methodologies and technologies that help people and organizations deal with the chronic and tough issues in research-based, intelligent and inspiring ways.

Specialties:Breaking down the walls between disciplines such as environmental, social, and economic approaches to create ideologies and methodologies that weave them all to change the way we live. This ideology and methodology applies to all areas: business development, business identity, strategy for all organizations - public, private and NGO.This starts at the individual level.Morwen is also an energy healer specializing in belief reconstruction leading to fulfilling lives.

```html
<!DOCTYPE html>
<html lang="en">
<head>
<meta charset="utf-8">
<title>Verdalux</title>
<link rel="stylesheet" href="https://fonts.googleapis.com/css2?family=PT+Sans+Narrow:wght@400;700&family=Arimo:wght@400;700&family=Ubuntu:wght@400&display=swap">
<style>
:root{
  --red:#d8393b;
  --red-dark:#c72c2e;
  --yellow:#f6b21b;
  --blue:#1a6fb5;
  --green:#0b8a5c;
  --orange:#f07d16;
  --ink:#222;
  --dark:#2a2a2a;
  --darker:#1d1d1d;
  --panel:#444;
  --grey-text:#777;
  --rule:#d9d9d9;
  --page:#f4f6f9;
}
*{box-sizing:border-box;margin:0;padding:0}
html,body{width:718px;height:1200px;overflow:hidden}
body{position:relative;background:linear-gradient(#fff 0,#fff 60px,var(--page) 400px,#fff 700px,#fff 1010px);font-family:Arimo,Arial,sans-serif;color:var(--ink)}
.abs{position:absolute}
.narrow{font-family:"PT Sans Narrow",Arial Narrow,sans-serif}
.ph{display:block}

/* header */
.site-header{left:0;top:0;width:718px;height:65px;background:#fff;border-top:2px solid var(--red);border-bottom:1px solid #ddd}
.brand{left:98px;top:18px;display:flex;align-items:center;gap:6px}
.brand-dot{width:12px;height:12px;border-radius:50%;background:var(--red)}
.brand-name{font-family:Ubuntu,sans-serif;font-size:24px;color:var(--blue)}
.nav{left:280px;top:-2px;height:65px;display:flex}
.nav a{display:flex;align-items:center;height:65px;padding:0 10px;font-size:8.5px;font-weight:700;color:#555;text-decoration:none;border-right:1px solid #eee}
.nav a.active{background:var(--red);color:#fff;padding:0 8px}

/* hero */
.hero{left:0;top:65px;width:718px;height:244px;background:linear-gradient(#d4d4d4,#ececec 60%,#e2e2e2)}
.hero-art{left:310px;top:15px;width:330px;height:229px;background:radial-gradient(ellipse at 55% 70%,#e9b9a0,#d9a68a 45%,rgba(220,200,190,0) 75%)}
.hero-card{left:82px;top:71px;width:216px;height:114px;background:var(--panel);border-left:8px solid var(--yellow);padding:16px 12px}
.hero-card h1{font-family:Arimo,sans-serif;font-weight:400;font-size:19px;line-height:25px;color:#fff}
.btn{display:inline-block;background:var(--red);color:#fff;font-weight:700;text-transform:uppercase}
.hero-card .btn{margin-top:9px;font-family:"PT Sans Narrow",sans-serif;font-weight:400;font-size:13px;padding:5px 6px}

/* projects */
.projects{left:82px;top:308px;width:552px;height:175px;background:#fff;box-shadow:0 2px 6px rgba(0,0,0,.12)}
.bar-head{height:26px;background:var(--dark);color:#fff;font-family:"PT Sans Narrow",sans-serif;font-size:17px;line-height:26px;padding-left:12px;border-left:6px solid var(--blue)}
.project{top:34px;width:168px}
.project .ph{width:168px;height:57px}
.project h3{margin-top:11px;font-family:Ubuntu,sans-serif;font-weight:400;font-size:12px;display:flex;justify-content:space-between;align-items:center;padding:0 2px 7px 4px;border-bottom:1px solid #e3e3e3}
.arrow{width:15px;height:15px;border-radius:50%;background:#4a525a;display:inline-flex;align-items:center;justify-content:center}
.project p{margin-top:9px;font-size:7px;line-height:12px;color:var(--grey-text)}

/* welcome */
.sec-title{font-family:"PT Sans Narrow",sans-serif;font-size:17px;color:var(--ink);display:flex;align-items:center;gap:6px}
.sec-title span{color:var(--blue)}
.mark{width:22px;height:22px;border-radius:50%;background:#9cc6e6}
.welcome-text{left:96px;top:526px;width:344px;font-size:7.2px;line-height:11.8px;color:#666;text-align:justify}
.read-more{left:402px;top:602px;font-size:7px;font-weight:700;font-style:italic;color:#555;text-decoration:underline}
.video{left:452px;top:519px;width:170px;height:92px;background:linear-gradient(135deg,#7b5a3a,#c9b8a0 55,#e6e0da)}
.video-art{width:170px;height:80px;background:linear-gradient(120deg,#6e4e32,#a08060 40%,#d9d2c9 70%,#efece8)}
.video-bar{height:12px;background:#ddd;display:flex;align-items:center;gap:4px;padding:0 3px;font-size:6px;color:#555}
.play{width:0;height:0;border-left:6px solid #333;border-top:4px solid transparent;border-bottom:4px solid transparent}
.track{flex:1;height:3px;background:#999;position:relative}
.track i{position:absolute;left:0;top:0;width:40%;height:3px;background:var(--red)}

/* columns */
.col-head{top:641px;height:30px;background:var(--dark);color:#fff;font-family:"PT Sans Narrow",sans-serif;font-size:17px;line-height:30px;padding-left:12px}
.col-box{top:682px;height:163px;border:1px solid var(--rule);background:#fff}
.date{left:0;top:0;width:66px;height:60px;background:var(--green);color:#fff;text-align:center;font-family:"PT Sans Narrow",sans-serif;font-size:21px;line-height:22px;padding-top:10px}
.date small{font-size:15px;display:block}
.news-lead{left:67px;top:10px;width:94px;font-family:"PT Sans Narrow",sans-serif;font-size:10.5px;line-height:14px;color:#555}
.news-body{left:16px;top:78px;width:140px;font-size:6.8px;line-height:12px;color:#888}
.small-btn{font-family:"PT Sans Narrow",sans-serif;font-size:7.5px;padding:5px 5px;border-radius:2px}
.post{font-size:6.8px;line-height:12px;color:#888}
.post b{color:#555;font-size:7px}
.post em{display:block;font-style:normal;color:var(--red)}
.social-head{left:452px;top:641px;width:170px;height:30px;background:var(--dark);border-left:6px solid var(--red)}
.tab{top:14px;font-size:9px;padding:3px 5px;color:#fff}
.tab.on{background:#fff;color:var(--blue)}
.social-box{left:452px;top:671px;width:170px;height:174px;border:1px solid var(--rule);background:#fff}
.fans{left:5px;top:20px;display:grid;grid-template-columns:repeat(5,28px);gap:4px 5px}
.fan{font-size:5px;color:#888;text-align:center}
.fan i{display:block;width:28px;height:27px;background:linear-gradient(#8c6c58,#5a4638)}
.like{left:48px;top:3px;font-size:5.5px;color:var(--blue);display:flex;gap:3px;align-items:center}
.like b{border:1px solid #ccc;background:#eef1f7;padding:1px 3px;font-weight:400;color:#3b5998}

/* gallery */
.gallery{left:93px;top:892px;width:529px;height:101px;border:1px solid #ddd;border-radius:4px;background:linear-gradient(#fff,#ececec)}
.gallery .ph{top:13px;width:145px;height:73px}
.g-nav{top:41px;width:16px;height:16px;border-radius:50%;background:#f2f2f2;border:1px solid #ccc}

/* footer */
.band{left:0;top:1014px;width:718px;height:7px;display:flex}
.band i{flex:1}
.site-footer{left:0;top:1021px;width:718px;height:161px;background:var(--dark)}
.f-title{font-family:"PT Sans Narrow",sans-serif;font-size:14px;color:#fff;padding-bottom:6px;border-bottom:1px solid #444}
.f-links{list-style:none;font-size:7px;line-height:13.6px;color:#ddd;margin-top:6px}
.f-about{font-size:7px;line-height:9.3px;color:#ddd;margin-top:7px;text-align:justify}
.field{width:131px;height:14px;background:#fff;border:1px solid #999;font-size:5.8px;color:#555;padding:3px 4px}
.squares{display:flex;gap:6px}
.squares i{width:13px;height:13px;border-radius:2px}
.copy{left:0;top:1182px;width:718px;height:18px;background:var(--darker);color:#ccc;font-size:5.8px;text-align:center;line-height:18px}
</style>
</head>
<body>

<header class="site-header abs">
  <div class="brand abs"><span class="brand-dot"></span><span class="brand-name">Verdalux</span></div>
  <nav class="nav abs">
    <a class="active">HOME</a><a>ABOUT</a><a>SERVICES</a><a>PROJECT</a><a>NEWS</a><a>BLOG</a><a>CONATCT US</a>
  </nav>
</header>

<section class="hero abs">
  <div class="hero-art abs" role="img" aria-label="Smiling painted fingertips of raised hands with speech bubbles naming the service areas"></div>
  <div class="hero-card abs">
    <h1>Company that houses diverse services</h1>
    <span class="btn">More Details</span>
  </div>
</section>

<section class="projects abs">
  <div class="bar-head">Recent Project Profiles</div>
  <article class="project abs" style="left:11px">
    <div class="ph" role="img" aria-label="Presenter at a whiteboard in a classroom" style="background:linear-gradient(90deg,#d9dcd8,#b8a89c 60%,#7a5a50)"></div>
    <h3 style="color:var(--blue)">Diam Nonummy <span class="arrow"><svg width="7" height="7" viewBox="0 0 7 7"><path d="M1 3.5h5M4 1.5l2 2-2 2" stroke="#fff" fill="none"/></svg></span></h3>
    <p>Consecttuera dipiscing elit, sed diam nonummy nibh euismod,Consecttuera dipiscing elit,</p>
  </article>
  <article class="project abs" style="left:190px">
    <div class="ph" role="img" aria-label="Colourful molecular model construction sticks" style="background:linear-gradient(120deg,#2c5a7a,#c85a3a 45%,#3a8ab0 75%,#d5c05a)"></div>
    <h3 style="color:var(--green)">Nostrud Exerci <span class="arrow"><svg width="7" height="7" viewBox="0 0 7 7"><path d="M1 3.5h5M4 1.5l2 2-2 2" stroke="#fff" fill="none"/></svg></span></h3>
    <p>Consecttuera dipiscing elit, sed diam nonummy nibh euismod,Consecttuera dipiscing elit,</p>
  </article>
  <article class="project abs" style="left:369px">
    <div class="ph" role="img" aria-label="Students gathered around a lab bench" style="background:linear-gradient(90deg,#5a4a3e,#9c8c7c 50%,#4e4238)"></div>
    <h3 style="color:var(--orange)">Feugiat Nulla <span class="arrow"><svg width="7" height="7" viewBox="0 0 7 7"><path d="M1 3.5h5M4 1.5l2 2-2 2" stroke="#fff" fill="none"/></svg></span></h3>
    <p>Consecttuera dipiscing elit, sed diam nonummy nibh euismod,Consecttuera dipiscing elit,</p>
  </article>
</section>

<h2 class="sec-title abs" style="left:92px;top:495px"><i class="mark"></i>Welcome to&nbsp;<span>Verdalux</span></h2>
<p class="welcome-text abs">Lorem ipsum dolor sit amet, consectetuer adipiscing elit, sed diam nonummy nibh euismod tincidunt ut laoreet d olore magna aliquam erat volutpat. Ut wisi enim ad minim veniam, quis nostrud exerci tation ullamcorper suscipit lobortis nisl ut aliquip ex ea commodo consequat. Duis autem vel eum iriure dolor in hendrerit in vulputate velit esse molestie consequat, vel illum dolore eu feugiat nulla facilisis at vero eros et accumsan et iusto odio digni ssim qui blandit praesent luptatum zzril delenit</p>
<a class="read-more abs">Read More</a>

<h2 class="sec-title abs" style="left:453px;top:494px">Verdalux&nbsp;<span>Video</span></h2>
<div class="video abs">
  <div class="video-art" role="img" aria-label="Video still of a workshop with a scientist and students"></div>
  <div class="video-bar"><span class="play"></span><span class="track"><i></i></span><span>01:56</span><span>menu</span></div>
</div>

<div class="col-head abs" style="left:93px;width:168px;border-left:8px solid var(--yellow)">RECENTS NEWS
  <svg class="abs" style="right:8px;top:10px" width="20" height="9" viewBox="0 0 20 9"><circle cx="4.5" cy="4.5" r="4.5" fill="#888"/><circle cx="15.5" cy="4.5" r="4.5" fill="#888"/><path d="M5.5 2.5l-2 2 2 2M14.5 2.5l2 2-2 2" stroke="#2a2a2a" fill="none"/></svg>
</div>
<div class="col-box abs" style="left:93px;width:168px">
  <div class="date abs">NOV<small>9th</small></div>
  <p class="news-lead abs">Consecttuera dipiscing elit, sed diam nonummy nibh euismod,</p>
  <p class="news-body abs">Consecttuera dipiscing elit, sed diam nonum my nibh euismod,Consecttuera dipiscing elit, Consecttuera dipiscing elit, sed diam nonum my nibh euismod,</p>
  <span class="btn small-btn abs" style="left:12px;top:135px">Read More</span>
</div>

<div class="col-head abs" style="left:272px;width:168px;border-left:8px solid var(--blue)">LATEST BLOG</div>
<div class="col-box abs" style="left:272px;width:168px;padding:8px 12px">
  <p class="post"><b>Consecttuera dipiscing elit,</b><em>12/2/2013</em>sed diam nonum my nibh euismod, Consec ttuera dipiscing elit, Consecttuera dipiscing elit, sed diam nonum</p>
  <p class="post" style="margin-top:4px"><b>Consecttuera dipiscing elit,</b><em>12/2/2013</em>sed diam nonum my nibh euismod, Consec ttuera dipiscing elit, Consecttuera dipiscing elit, sed diam nonum</p>
  <span class="btn small-btn abs" style="left:12px;top:135px">Read More</span>
</div>

<div class="social-head abs">
  <span class="tab on abs" style="left:15px">Circlehub</span>
  <span class="tab abs" style="left:65px">Chirpline</span>
</div>
<div class="social-box abs">
  <span class="abs" style="left:10px;top:4px;width:9px;height:9px;border-radius:50%;background:#9cc6e6"></span>
  <div class="like abs"><b>Like</b>108 people like Verdalux</div>
  <div class="fans abs">
    <div class="fan"><i></i>Lena</div><div class="fan"><i></i>Ravi</div><div class="fan"><i></i>Lena</div><div class="fan"><i></i>Ravi</div><div class="fan"><i></i>Lena</div>
    <div class="fan"><i></i>Lena</div><div class="fan"><i></i>Ravi</div><div class="fan"><i></i>Lena</div><div class="fan"><i></i>Ravi</div><div class="fan"><i></i>Lena</div>
    <div class="fan"><i></i>Lena</div><div class="fan"><i></i>Ravi</div><div class="fan"><i></i>Lena</div><div class="fan"><i></i>Ravi</div><div class="fan"><i></i>Lena</div>
  </div>
  <div class="abs" style="left:5px;top:148px;width:158px;border-top:1px solid #ddd;padding-top:6px;font-size:5.5px;color:#666;display:flex;justify-content:space-between;align-items:center">
    <span><span style="display:inline-block;width:7px;height:7px;background:#3b5998;vertical-align:middle"></span> Circlehub social plugin</span>
    <span style="font-size:8px;font-weight:700;color:var(--blue)">Join Us!</span>
  </div>
</div>

<h2 class="sec-title abs" style="left:92px;top:862px"><i class="mark"></i>Photo&nbsp;<span>Gallery</span></h2>
<div class="gallery abs">
  <span class="g-nav abs" style="left:-6px"></span>
  <div class="ph abs" style="left:24px;background:linear-gradient(90deg,#6a5a52,#a89890 50%,#5e5048)" role="img" aria-label="Group of participants standing in a hall"></div>
  <div class="ph abs" style="left:192px;background:linear-gradient(120deg,#3a4a6a,#d8dce4 50%,#7a6a60)" role="img" aria-label="Students working around a table"></div>
  <div class="ph abs" style="left:360px;background:linear-gradient(120deg,#e8e8e8,#5a4e48 50%,#cfd3da)" role="img" aria-label="Young people writing on posters"></div>
  <span class="g-nav abs" style="right:-6px"></span>
</div>

<div class="band abs"><i style="background:var(--red)"></i><i style="background:var(--yellow)"></i><i style="background:var(--blue)"></i><i style="background:var(--green)"></i></div>

<footer class="site-footer abs">
  <div class="abs" style="left:94px;top:15px;width:63px">
    <h4 class="f-title" style="font-weight:400">Quick Links</h4>
    <ul class="f-links"><li>Home</li><li>About Us</li><li>Services</li><li>Project</li><li>News</li><li>Blog</li><li>Contact Us</li></ul>
  </div>
  <div class="abs" style="left:179px;top:15px;width:156px">
    <h4 class="f-title" style="font-weight:400">About Morwen</h4>
    <p class="f-about">Morwen has spent 30 years leading expeditions into the future. Morwen has a special interest in exploring the changing business, social and cultural landscapes and frontiers, uncovering uncharted territory and unleashing hidden potential – within the person, family, organization, community, business or marketplace. Morwen thrives on experimentation that has led to blended eastern help people and organizations deal .....</p>
    <span class="btn small-btn" style="margin-top:8px">Read More</span>
  </div>
  <div class="abs" style="left:359px;top:15px;width:131px">
    <h4 class="f-title" style="font-weight:400">Signup to our Newsletter</h4>
    <p style="font-size:7px;line-height:10.5px;color:#ddd;margin-top:6px">Lorem ipsum dolor sit amet consec tetur adipisicing elitsed</p>
    <div class="field" style="margin-top:6px">Enter your emil here</div>
    <span class="btn small-btn" style="margin-top:7px">Subscribe</span>
    <div style="display:flex;align-items:center;gap:12px;margin-top:16px">
      <span class="narrow" style="font-size:14px;color:#fff">Follow us</span>
      <div class="squares"><i style="background:#3b5998"></i><i style="background:#2a9ad6"></i><i style="background:#5a5a5a"></i><i style="background:#d0203a"></i></div>
    </div>
  </div>
  <div class="abs" style="left:514px;top:40px;display:flex;align-items:center;gap:6px">
    <span style="width:14px;height:14px;border-radius:50%;background:var(--red)"></span>
    <span style="font-family:Ubuntu,sans-serif;font-size:26px;color:var(--blue)">Verdalux</span>
  </div>
  <p class="abs" style="left:500px;top:123px;width:121px;text-align:right;font-size:7px;color:#fff">Email : info@verdalux.com</p>
  <p class="abs" style="left:470px;top:135px;width:151px;text-align:right;font-size:11px;font-weight:700;color:var(--red)">Phone: 0123-987654</p>
</footer>

<div class="copy abs">© 2013 Verdalux- Copyright applies to all content of this website.</div>

</body>
</html>
```